!!! THIS PROJECT IS FOR ODETTE ONLY !!!
Hi Odette,
Hope you are well.
Please help me to create a new poster for my new dishes.
Poster size is A2 (420mmx595mm)
I want 1 poster design to showcase all 3 new dishes.
1. Bánh Mì $9.50 (I've sent all photos of this but you don't need to use all photos - its all up to you to make the design fit)
- Lemongrass Chicken
- Lemongrass Beef
- BBQ Pork
- Tofu
2. Egg Noodle with Crispy Skin Chicken (With Soup / Dry) $16.50
3. Rice with Crispy Skin Chicken. $16.50

```html
<!DOCTYPE html>
<html lang="en">
<head>
<meta charset="utf-8">
<title>New Dishes Poster</title>
<link rel="stylesheet" href="https://fonts.googleapis.com/css2?family=Comic+Neue:wght@400;700&display=swap">
<style>
  :root {
    --page-bg: #ecebe8;
    --poster-red: #ec1c24;
    --poster-yellow: #ffd200;
    --ink-white: #ffffff;
    --photo-dark: #2b2b2b;
    --photo-mid: #454545;
    --dash-dark: #1a1a1a;
  }
  html, body {
    margin: 0;
    padding: 0;
    width: 1200px;
    height: 2394px;
    overflow: hidden;
    background: var(--page-bg);
  }
  .poster {
    position: absolute;
    left: 100px;
    top: 489px;
    width: 1000px;
    height: 1416px;
    overflow: hidden;
    box-shadow: 0 10px 30px rgba(0,0,0,0.25);
  }
  .poster svg { display: block; width: 100%; height: 100%; }
  .field-red { fill: var(--poster-red); }
  .brush-field { fill: var(--poster-yellow); }
  .inner-frame { fill: none; stroke: var(--ink-white); stroke-width: 2.5; }
  .ring-yellow { fill: var(--poster-yellow); }
  .ring-white { fill: var(--ink-white); }
  .dash-orbit { fill: none; stroke: var(--dash-dark); stroke-width: 2; stroke-dasharray: 5 3; }
  .photo { fill: url(#photoTone); }
  .divider-bar { fill: var(--ink-white); }
  .dish-title {
    font-family: "Comic Neue", "Comic Sans MS", cursive;
    font-weight: 700;
    font-size: 25.5px;
    fill: var(--poster-yellow);
    text-anchor: middle;
  }
  .dish-detail {
    font-family: "Comic Neue", "Comic Sans MS", cursive;
    font-weight: 400;
    font-size: 24px;
    fill: var(--ink-white);
    text-anchor: middle;
  }
</style>
</head>
<body>
<div class="poster">
  <svg viewBox="0 0 738 1045" xmlns="http://www.w3.org/2000/svg">
    <defs>
      <radialGradient id="photoTone" cx="50%" cy="45%" r="60%">
        <stop offset="0%" stop-color="#454545"/>
        <stop offset="100%" stop-color="#2b2b2b"/>
      </radialGradient>
      <filter id="softEdge" x="-10%" y="-10%" width="120%" height="120%">
        <feGaussianBlur stdDeviation="5"/>
      </filter>
    </defs>

    <rect class="field-red" width="738" height="1045"/>
    <path class="brush-field" filter="url(#softEdge)" role="img" aria-label="Painted yellow brush stroke sweeping across the red background"
      d="M-40 -40 H780 V280 C690 325 625 385 582 450 C540 512 498 562 440 610 C390 650 342 680 300 672 C260 664 232 640 210 610 C182 560 142 522 100 500 C62 480 30 462 -40 445 Z"/>

    <rect class="inner-frame" x="25" y="25" width="688" height="995"/>

    <circle class="dash-orbit" cx="350" cy="347" r="262"/>
    <circle class="dash-orbit" cx="496" cy="186" r="132"/>
    <circle class="dash-orbit" cx="216" cy="543" r="130"/>

    <circle class="ring-yellow" cx="350" cy="347" r="232"/>
    <circle class="ring-white" cx="350" cy="347" r="221"/>
    <circle class="photo" cx="350" cy="347" r="217" role="img" aria-label="Rice with crispy skin chicken, cucumber, carrot and lettuce on a white plate"/>

    <circle class="ring-yellow" cx="496" cy="186" r="120"/>
    <circle class="ring-white" cx="496" cy="186" r="110"/>
    <circle class="photo" cx="496" cy="186" r="106" role="img" aria-label="Egg noodle soup bowl beside crispy skin chicken"/>

    <circle class="ring-yellow" cx="216" cy="543" r="118"/>
    <circle class="ring-white" cx="216" cy="543" r="108"/>
    <circle class="photo" cx="216" cy="543" r="104" role="img" aria-label="Banh mi filled with grilled meat and herbs on a white plate"/>

    <text class="dish-title" x="369" y="712">Bánh Mì $9.50</text>
    <text class="dish-detail" x="369" y="748">Lemongrass Chicken | Lemongrass Beef</text>
    <text class="dish-detail" x="369" y="778">BBQ Pork | Tofu</text>

    <rect class="divider-bar" x="158" y="808" width="422" height="2" role="img" aria-label="Decorative divider"/>

    <text class="dish-title" x="369" y="856">Egg Noodle with Crispy Skin Chicken</text>
    <text class="dish-detail" x="369" y="887">(With Soup / Dry) $16.50</text>

    <rect class="divider-bar" x="158" y="916" width="422" height="2" role="img" aria-label="Decorative divider"/>

    <text class="dish-title" x="369" y="964">Rice with Crispy Skin Chicken</text>
    <text class="dish-detail" x="369" y="995">$16.50</text>
  </svg>
</div>
</body>
</html>
```